Armored courier complete website design
HALVORSEN
Armored courier complete website design - Security
Creative Brief
Security
www.halvorsenllc-example.com
Local armored transportation company for packages, documents, deposits, ATM's and banks. quillmark482 created original logo and personal font from zentaflow. SERVICES OFFERED BY THE HALVORSEN COMPANY (1.) Courier (a.) Cash Logistics (i.) Critical Delivery (ii.) Armored Courier Services (b.) Pharmaceutical (c.) Medical Logistics (d.) Retail & Commercial Deposit Delivery & Change Order Return Service (e.) Legal (i.) Document Delivery (ii.) Critical Courier (2.) ATM Services (a.) Installation & Removal (b.) Cash Replenishment & Deposit Removal (c.) Maintenance & Repair (i.) First Line (d.) Physical Surroundings Repair (i.) Carousel (ii.) Signage (iii.) Pilons (e.) Custom ATM Branding Solutions (f.) ATM Cleaning & Detailing (3.) Security Guard Services (a.) Corporate Security (b.) Industrial (c.) Retail (d.) Tourism & Special Events (4.) Investigative Services (a.) Corporate Investigations (b.) Workers’ Compensation Fraud Investigations (c.) Retail & Industrial (5.) Secure-Area Cleaning Services (a.) Banks & Credit Unions (b.) Industrial & Commercial (6.) Logistics (a.) Contract Logistics (b.) Critical Parts & Product Logistics (7.) Document Destruction (a.) Scheduled Programs (b.) Short term, Single Project
Would like a design similar to Belvane.com but feel free to expand from that idea. Centralized text box for images and information. Promote strength through imagery. Do not want a cookie cutter site like everyone else, i.e. Ostrel and Kellworth
left side
www.belvane.com
http://www.ostrelworld-example.com/cash-services/en
http://kellworthsecure-example.com/
Copy for each subject can be provided. Ostrelworld has a good layout of services provided, company, careers, contact us Contact us is very important -Company -Services - - - -Careers -Contact us
Halvorsen Halvorsen
The instructions provided with our latest brief updates should assist everyone in tweaking and completing the HALVORSEN design. The simplicity and elegance similar to belvane.com is all we're after. Clean lines, dark shading, stainless steel used as indicated, watermarks, chiseled edging, sharp relative images and clear/smoked borders placed as directed is what we are currently seeking. Thank you much for your efforts to date and we look forward to seeing everyone's updates per the brief updates provided below.
#96 is closest to what we are looking for. The center, scrolling buttons would be a little smaller, no border but suspended with a white, small description text at the top of each. The large, background image would have a small text description at the upper right only. This description/button could be clicked on in reference to the photo for navigation purposes. Thank you for your hard work. Much appreciated.
The bottom of the page should be entirely black with a slight fade at the top. This should cover the entire bottom of the page and be about a quarter to 1/3rd in height. The side bar should slightly bleed into this dark space. Only very small text disclosures, etc. will be placed in this black area. Thank you.
Please, no shield references at top of the navigation bar. Rectangular only. Thank you in advance.
Also, on the side, navigation bar please only put the name HALVORSEN at the top and utilize our logo at the bottom in a darker, chiseled watermark. The company name should be separated from the navigation bars via a thin line. Border the side bar identical to draft #96, i.e. transparent, and use the same darker, shaded stainless steel background behind all text as draft #96. In addition, the emphasis will be on scrolling images in the background so the width and text of navigation side bar can smaller and tighter but longer in length. Thank you for your efforts!
#96 is closest so far to what we are looking for. Left navigation bar is key. Refer all designs to Belvane.com this is the look we are going for. Spend the time on the little things, a simple design that we are looking for only works with with high quality nav bars and animation. Thank you all for your hard work!

```html
<!DOCTYPE html>
<html lang="en">
<head>
<meta charset="utf-8">
<title>Halvorsen – Armored Courier</title>
<link rel="stylesheet" href="https://fonts.googleapis.com/css2?family=Roboto:wght@400;500;700&display=swap">
<style>
  :root{
    --black:#070707;
    --ink:#0d0d0e;
    --white:#ffffff;
    --soft:#d6d6d6;
    --muted:#a9a9a9;
    --amber:#f0a43a;
    --steel-top:rgba(40,42,46,.92);
    --steel-bottom:rgba(18,19,21,.9);
    --active:#5b5d62;
    --line:#555;
    --circle:rgba(12,12,14,.82);
    --input:#ffffff;
    --button:#1c1c1c;
  }
  *{box-sizing:border-box;margin:0;padding:0}
  html,body{width:1200px;height:1062px;overflow:hidden;background:var(--black)}
  body{font-family:"Roboto",Arial,sans-serif;color:var(--white);position:relative}

  .hero{position:absolute;left:0;top:0;width:1200px;height:712px;
    background:
      radial-gradient(ellipse at 78% 40%,rgba(120,170,220,.55),transparent 45%),
      radial-gradient(ellipse at 60% 25%,rgba(200,210,225,.35),transparent 40%),
      linear-gradient(90deg,#1f2328 0%,#47505a 30%,#6e7884 55%,#2c333c 80%,#3b4149 100%);}

  .footer{position:absolute;left:0;top:640px;width:1200px;height:422px;
    background:linear-gradient(180deg,rgba(7,7,7,0) 0,var(--black) 70px,var(--black) 100%)}

  .sidebar{position:absolute;left:69px;top:66px;width:250px;height:650px;
    background:linear-gradient(180deg,var(--steel-top),var(--steel-bottom));
    border:1px solid rgba(255,255,255,.12)}
  .brand{display:flex;align-items:center;justify-content:center;gap:10px;
    height:130px;border-bottom:1px solid var(--line);margin:0 18px}
  .brand-mark{width:14px;height:14px;background:var(--white)}
  .brand-name{font-size:28px;font-weight:700;letter-spacing:2px;color:var(--white)}
  .nav{list-style:none;margin-top:44px}
  .nav li{position:relative;height:37px;line-height:37px;font-size:15px;font-weight:700;
    text-align:right;padding-right:80px;letter-spacing:.5px}
  .nav li::after{content:"›";position:absolute;right:52px;top:-1px;font-size:22px;font-weight:400}
  .nav li.active{background:var(--active)}

  .services{position:absolute;top:455px;left:351px;display:flex;gap:35px}
  .service{width:144px;height:144px;border-radius:50%;background:var(--circle);
    display:flex;flex-direction:column;align-items:center;justify-content:center;gap:12px}
  .service svg{width:44px;height:44px}
  .service-label{font-size:15px;color:var(--amber);letter-spacing:.5px}
  .more{position:absolute;left:1075px;top:503px;font-size:40px;color:var(--white)}

  .section-title{position:absolute;top:728px;font-size:22px;color:var(--white)}
  .links{position:absolute;top:796px;list-style:none;font-size:14px;color:var(--soft)}
  .links li{height:34.5px}
  .divider{position:absolute;top:735px;width:1px;height:235px;background:#2a2a2a}

  .signup{position:absolute;left:345px;top:800px;display:flex}
  .signup-input{width:219px;height:40px;background:var(--input);color:#555;font-size:14px;
    padding:0 12px;line-height:40px}
  .signup-button{width:115px;height:40px;background:var(--button);color:var(--white);
    font-size:14px;line-height:40px;text-align:center}
  .social{position:absolute;left:345px;top:870px;display:flex;gap:12px}
  .social span{width:22px;height:22px;background:var(--white);border-radius:3px}
  .share{position:absolute;left:345px;top:922px;font-size:14px;color:var(--soft)}

  .phone{position:absolute;left:737px;top:800px;width:76px;height:150px;border:2px solid #666;
    border-radius:10px;background:#111}
  .phone::before{content:"";position:absolute;left:6px;top:18px;right:6px;bottom:24px;background:#1d1f22}
  .app-copy{position:absolute;left:857px;top:800px;width:260px;font-size:14px;line-height:19px;color:var(--soft)}
  .badge{position:absolute;left:857px;width:101px;height:28px;background:#1a1a1a;border:1px solid #888;border-radius:4px}

  .copyright{position:absolute;left:0;top:1001px;width:1200px;text-align:center;font-size:13px;color:var(--soft)}
</style>
</head>
<body>
  <div class="hero" role="img" aria-label="Background photo: businessman holding a glowing globe surrounded by digital icons, server room behind"></div>
  <div class="footer"></div>

  <aside class="sidebar">
    <div class="brand"><span class="brand-mark"></span><span class="brand-name">HALVORSEN</span></div>
    <ul class="nav">
      <li>COMPANY</li>
      <li class="active">SERVICES</li>
      <li>CAREERS</li>
      <li>BLOG</li>
      <li>CONTACT</li>
    </ul>
  </aside>

  <div class="services">
    <div class="service">
      <svg viewBox="0 0 44 44" fill="#fff"><rect x="2" y="10" width="24" height="20"/><path d="M28 16h8l6 7v7H28z"/><circle cx="11" cy="33" r="4"/><circle cx="34" cy="33" r="4"/></svg>
      <span class="service-label">COURIER</span>
    </div>
    <div class="service">
      <svg viewBox="0 0 44 44"><rect x="2" y="11" width="40" height="22" fill="none" stroke="#fff" stroke-width="3"/><circle cx="22" cy="22" r="6" fill="#fff"/></svg>
      <span class="service-label">ATM</span>
    </div>
    <div class="service">
      <svg viewBox="0 0 44 44" fill="#fff"><path d="M16 4h12l-3 7h-6z"/><path d="M19 12h6c9 4 13 14 13 20 0 6-6 8-16 8S6 38 6 32c0-6 4-16 13-20z"/></svg>
      <span class="service-label">SECURITY</span>
    </div>
    <div class="service">
      <svg viewBox="0 0 44 44"><circle cx="18" cy="18" r="12" fill="none" stroke="#fff" stroke-width="4"/><path d="M27 27l13 13" stroke="#fff" stroke-width="6" stroke-linecap="round"/></svg>
      <span class="service-label">INVESTIGATIVE</span>
    </div>
  </div>
  <div class="more">»</div>

  <h2 class="section-title" style="left:75px;font-weight:400">Contact Details</h2>
  <ul class="links" style="left:75px">
    <li>Corporate</li><li>Responsibility</li><li>Travel Agent</li><li>Affiliate Program</li><li>Press Room</li>
  </ul>
  <ul class="links" style="left:224px">
    <li>Site Index</li><li>Help</li><li>Contact us</li><li>Careers</li>
  </ul>
  <div class="divider" style="left:311px"></div>

  <h2 class="section-title" style="left:345px;font-weight:400">Newsletters &amp; Offers</h2>
  <div class="signup"><div class="signup-input">Your email address</div><div class="signup-button">Subscribe</div></div>
  <div class="social"><span></span><span></span><span></span><span></span><span></span><span></span></div>
  <p class="share">Share your stories on Halvorsen.com</p>
  <div class="divider" style="left:708px"></div>

  <h2 class="section-title" style="left:734px;font-weight:400">Enjoy Our Mobile App!</h2>
  <div class="phone"></div>
  <p class="app-copy">Unlimited access to the world of Ashcombe wherever you go.</p>
  <div class="badge" style="top:857px"></div>
  <div class="badge" style="top:892px"></div>

  <p class="copyright">© 2015 All Rights are Reserved by Halvorsen LLC.</p>
</body>
</html>
```